Velor Stationery Design

We need Business Card, Letterhead, #10 Envelope , 3" x 4" Mailing Label, and email signature block. Also need "Aircraft Services" added small under the logo on everything except the email signature block. "Aircraft Services" should be in a simple font to to conflict with or distract from the logo. Our address info is:
4817 Marlow Bend NW
Kennesaw, GA 30144
P 555.284.6613
C 555.284.6613 (for biz cards only)
pete@velorjet.example (for biz cards only)
Website velorjet.example
Feel free to play around with colors but I expect that black or gray will work best for the address/phone info etc.

Target Market(s)

Aircraft owners

Industry/Entity Type

Aviation

Colors

Designer to choose only greyscale colors for use in the design.

Requirements
Must have
• Clean and sophisticated design -

```html
<!DOCTYPE html>
<html lang="en">
<head>
<meta charset="utf-8">
<title>Velor Aircraft Services — Letterhead</title>
<link href="https://fonts.googleapis.com/css2?family=Figtree:wght@400;500;600&family=Montserrat:wght@600;800&display=swap" rel="stylesheet">
<style>
  :root {
    --brand-blue: #0a78dc;
    --ink: #474747;
    --ink-soft: #6a6a6a;
    --rule-gray: #9a9a9a;
    --paper: #ffffff;
    --backdrop: #d9d9d9;
  }
  * { box-sizing: border-box; margin: 0; padding: 0; }
  html, body {
    width: 1200px; height: 1200px; overflow: hidden;
    background: var(--backdrop);
  }
  .letterhead {
    position: absolute; left: 175px; top: 20px;
    width: 851px; height: 1158px;
    background: var(--paper);
    font-family: "Figtree", "Helvetica Neue", Arial, sans-serif;
    color: var(--ink);
    box-shadow: 0 6px 24px rgba(0,0,0,0.18);
    overflow: hidden;
  }
  .brand {
    position: absolute; left: 0; right: 0; top: 50px;
    text-align: center;
  }
  .brand-name {
    font-family: "Montserrat", Arial, sans-serif;
    font-weight: 800; font-size: 92px; line-height: 0.86;
    letter-spacing: 5px; text-transform: uppercase;
    color: var(--brand-blue);
  }
  .brand-tagline {
    margin-top: 6px;
    font-family: "Montserrat", Arial, sans-serif;
    font-weight: 600; font-size: 16.5px; letter-spacing: 2.8px;
    text-transform: uppercase; color: var(--ink);
  }
  .salutation {
    position: absolute; left: 60px; top: 264px;
    font-weight: 600; font-size: 27.5px; letter-spacing: 0.3px;
    color: var(--brand-blue);
  }
  .letter-body {
    position: absolute; left: 60px; top: 321px; width: 730px;
    font-size: 19.6px; line-height: 23.6px; letter-spacing: -0.35px;
    color: var(--ink);
  }
  .letter-body p + p { margin-top: 23.6px; }
  .line {
    display: block; white-space: nowrap;
    text-align: justify; text-align-last: justify;
  }
  .line.last { text-align-last: left; }
  .sign-off { position: absolute; left: 69px; top: 770px; }
  .signer-name { font-size: 12px; color: var(--ink); }
  .signer-title { font-size: 9.5px; color: var(--ink-soft); margin-top: 3px; }
  .signature-area {
    position: absolute; left: 61px; top: 806px; width: 188px; height: 84px;
    background: linear-gradient(135deg, #f4f4f4, #e6e6e6);
    border-radius: 4px;
  }
  .contact {
    position: absolute; left: 58px; top: 1024px;
    font-size: 25px; line-height: 23px; color: var(--ink); font-style: normal;
  }
  .contact-row { display: flex; align-items: flex-start; gap: 10px; }
  .contact-row + .contact-row { margin-top: 9px; }
  .contact-row svg { flex: none; margin-top: 1px; }
  .footer-band {
    position: absolute; left: 0; bottom: 0; width: 851px; height: 54px;
  }
  .footer-url {
    position: absolute; right: 105px; bottom: 17px;
    font-family: "Montserrat", Arial, sans-serif;
    font-weight: 600; font-size: 19px; letter-spacing: 6.4px;
    text-transform: uppercase; color: var(--paper);
  }
</style>
</head>
<body>
  <main class="letterhead">
    <header class="brand">
      <div class="brand-name">Velor</div>
      <div class="brand-tagline">Aircraft Services</div>
    </header>

    <h1 class="salutation">Dear Mr. Hale,</h1>

    <section class="letter-body">
      <p>
        <span class="line">Lorem ipsum dolor sit amet, consectetuer adipiscing elit, sed diam nonummy nibh</span>
        <span class="line">euismod tincidunt ut laoreet dolore magna aliquam erat volutpat. Ut wisi enim ad</span>
        <span class="line">minim veniam, quis nostrud exerci tation ullamcorper suscipit lobortis nisl ut</span>
        <span class="line last">aliquip ex ea commodo consequat. Duis autem vel eum iriure dolor in</span>
        <span class="line">&nbsp;hendrerit in vulputate velit esse molestie consequat, vel illum dolore eu feugiat</span>
        <span class="line">nulla facilisis at vero eros et accumsan et iusto odio dignissim qui blandit praesent</span>
        <span class="line last">luptatum zzril delenit augue duis dolore te feugait nulla facilisi.</span>
      </p>
      <p>
        <span class="line">Lorem ipsum dolor sit amet, cons ectetuer adipiscing elit, sed diam nonummy</span>
        <span class="line">nibh euismod tincidunt ut laoreet dolore magna aliquam erat volutpat. Ut wisi</span>
        <span class="line">Lorem ipsum dolor sit amet, consectetuer adipiscing elit, sed diam nonummy nibh</span>
        <span class="line">euismod tincidunt ut laoreet dolore magna aliquam erat volutpat. Ut wisi enim ad</span>
        <span class="line">minim veniam, quis nostrud exerci tation ullamcorper suscipit lobortis nisl ut</span>
        <span class="line">aliquip ex ea commodo consequat. Duis autem vel eum iriure dolor in hendrerit in</span>
        <span class="line">vulputate velit esse molestie consequat,Lorem ipsum dolor sit amet, cons</span>
        <span class="line">ectetuer adipiscing elit, sed diam nonummy nibh euismod tincidunt ut laoreet</span>
        <span class="line last">dolore magna aliquam erat volutpat.</span>
      </p>
    </section>

    <div class="sign-off">
      <div class="signer-name">Alan Reyes</div>
      <div class="signer-title">Office Manager</div>
    </div>
    <div class="signature-area" role="img" aria-label="Handwritten signature of the office manager"></div>

    <address class="contact">
      <div class="contact-row">
        <svg width="24" height="24" viewBox="0 0 24 24" aria-hidden="true">
          <path fill="var(--brand-blue)" d="M6.6 10.8a15.1 15.1 0 0 0 6.6 6.6l2.2-2.2a1 1 0 0 1 1-.25 11.4 11.4 0 0 0 3.6.57 1 1 0 0 1 1 1V20a1 1 0 0 1-1 1A17 17 0 0 1 3 4a1 1 0 0 1 1-1h3.5a1 1 0 0 1 1 1c0 1.25.2 2.450.57 3.57a1 1 0 0 1-.25 1z"/>
        </svg>
        <span>P 555.284.6613</span>
      </div>
      <div class="contact-row">
        <svg width="24" height="32" viewBox="0 0 24 32" aria-hidden="true">
          <path fill="var(--brand-blue)" d="M12 1C6 1 1.5 5.4 1.5 11.2 1.5 18.5 12 31 12 31s10.5-12.5 10.5-19.8C22.5 5.4 18 1 12 1zm0 15.2a5 5 0 1 1 0-10 5 5 0 0 1 0 10z"/>
        </svg>
        <span>4817 Marlow Bend NW<br>Kennesaw, GA 30144</span>
      </div>
    </address>

    <svg class="footer-band" viewBox="0 0 851 54" preserveAspectRatio="none" aria-hidden="true">
      <path fill="var(--rule-gray)" d="M0 18 H392 C402 18 408 18 418 12 L414 18 C406 25 400 28 388 28 H0 Z"/>
      <path fill="var(--brand-blue)" d="M0 31 H398 C414 31 422 27 434 18 C448 7 456 0 472 0 H851 V54 H0 Z"/>
    </svg>
    <div class="footer-url">velorjet.example</div>
  </main>
</body>
</html>
```